Corwin Hale

20 Year Licensed Master Barber specializing in:
men/women cuts, Grooming, Straight razor Shaving and tape line enhancement, beard grooming, eye brow enhancement, South of France, Hot Towel Treatments, Scalp, Blow outs, Shags, Custom Design,RazorCuts,Shear Cuts, Bobs, Perms, Relaxers, Shoe Shine.
Please create a wonderful business card incorporating all the info above and selecting one of the photos. Please be creative.

Barber

```html
<!DOCTYPE html>
<html lang="en">
<head>
<meta charset="UTF-8">
<title>Corwin Hale – Master Barber Business Card</title>
<link href="https://fonts.googleapis.com/css2?family=Lato:wght@400;700;900&display=swap" rel="stylesheet">
<style>
  :root {
    --stage: #3b3230;
    --card-black: #050505;
    --card-white: #ffffff;
    --text-light: #f1f1f1;
    --accent-red: #d0141c;
    --brand-navy: #27307a;
    --brand-blue: #2a6fc0;
    --text-dark: #111111;
    --photo-warm: #6b5446;
    --photo-mid: #3c3f4a;
    --photo-dark: #16171c;
  }
  * { box-sizing: border-box; margin: 0; padding: 0; }
  html, body {
    width: 1200px; height: 716px; overflow: hidden;
    background: var(--stage);
    font-family: "Lato", sans-serif;
  }
  .stage {
    position: relative; width: 1200px; height: 716px;
    display: flex; align-items: center; justify-content: center; gap: 40px;
  }
  .card {
    position: relative; width: 540px; height: 309px;
    border-radius: 6px; overflow: hidden;
    box-shadow: 0 14px 30px rgba(0,0,0,0.45);
  }

  /* Services side */
  .card-services { background: var(--card-black); color: var(--text-light); }
  .services-heading {
    position: absolute; left: 30px; top: 26px; z-index: 2;
    color: var(--accent-red); font-size: 13px; font-weight: 400;
  }
  .services-list {
    position: absolute; left: 30px; top: 50px; z-index: 2;
    list-style: none; font-size: 13px; line-height: 17.5px;
  }
  .services-list li::before {
    content: "\203A"; margin-right: 8px; color: var(--text-light); font-size: 11px;
  }
  .services-list .continued { padding-left: 14px; }
  .services-list .continued::before { content: none; }
  .barber-photo {
    position: absolute; left: 220px; top: 95px; width: 320px; height: 214px;
    background:
      radial-gradient(ellipse 38% 45% at 40% 45%, var(--photo-warm) 0%, rgba(107,84,70,0) 100%),
      radial-gradient(ellipse 55% 60% at 50% 55%, var(--photo-mid) 0%, var(--photo-dark) 55%, rgba(5,5,5,0) 100%);
  }

  /* Brand & contact side */
  .card-contact { background: var(--card-white); color: var(--text-dark); }
  .card-contact::after {
    content: ""; position: absolute; left: 0; right: 0; bottom: 0; height: 3px;
    background: var(--brand-navy);
  }
  .brand {
    position: absolute; left: 250px; top: 70px; width: 230px; height: 130px;
    display: flex; align-items: center; justify-content: center; gap: 12px;
  }
  .brand-mark {
    flex: none; width: 44px; height: 44px; border-radius: 50%;
    background: var(--brand-blue);
  }
  .brand-name {
    font-size: 30px; line-height: 32px; font-weight: 900;
    color: var(--brand-navy); text-transform: uppercase; letter-spacing: 1px;
  }
  .contact-row {
    position: absolute; left: 30px; right: 30px; bottom: 30px;
    display: flex; justify-content: space-between; align-items: center;
    font-size: 15px;
  }
  .contact-item { display: flex; align-items: center; gap: 6px; }
  .contact-item svg { width: 13px; height: 13px; fill: var(--accent-red); }
</style>
</head>
<body>
<main class="stage">

  <section class="card card-services">
    <div class="barber-photo" role="img" aria-label="Painted-style portrait collage of the barber in glasses with a barber pole and two suited figures behind"></div>
    <h2 class="services-heading">20 Year Licensed Master Barber specializing in:</h2>
    <ul class="services-list">
      <li>Men/women cuts</li>
      <li>Grooming</li>
      <li>Straight razor Shaving</li>
      <li class="continued">and tape line enhancement</li>
      <li>Beard grooming</li>
      <li>Eye brow enhancement</li>
      <li>Hot Towel Treatments</li>
      <li>Scalp | Blow outs | Shags</li>
      <li>Custom Design</li>
      <li>RazorCuts</li>
      <li>Shear Cuts</li>
      <li>Bobs | Perms | Relaxers</li>
      <li>Shoe Shine.</li>
    </ul>
  </section>

  <section class="card card-contact">
    <div class="brand">
      <span class="brand-mark"></span>
      <span class="brand-name">Corwin<br>Hale</span>
    </div>
    <div class="contact-row">
      <span class="contact-item">
        <svg viewBox="0 0 24 24" aria-hidden="true"><path d="M12 2a7 7 0 0 0-7 7c0 5 7 13 7 13s7-8 7-13a7 7 0 0 0-7-7zm0 9.5A2.5 2.5 0 1 1 12 6.5a2.5 2.5 0 0 1 0 5z"/></svg>
        Your address
      </span>
      <span class="contact-item">
        <svg viewBox="0 0 24 24" aria-hidden="true"><path d="M6.6 10.8a15 15 0 0 0 6.6 6.6l2.2-2.2a1 1 0 0 1 1-.25 11.4 11.4 0 0 0 3.6.57 1 1 0 0 1 1 1V20a1 1 0 0 1-1 1A17 17 0 0 1 3 4a1 1 0 0 1 1-1h3.5a1 1 0 0 1 1 1c0 1.25.2 2.45.57 3.6a1 1 0 0 1-.25 1z"/></svg>
        000 000 0000
      </span>
      <span class="contact-item">
        <svg viewBox="0 0 24 24" aria-hidden="true"><path d="M2 5h20v14H2zm2 2v.5l8 5 8-5V7l-8 5z"/></svg>
        Email@xyz.com
      </span>
    </div>
  </section>

</main>
</body>
</html>
```